Business Card Design

We like to use greens as you will see in our logo (but not TOO much green). We are a Dental Clinic in a somewhat eccentric community. We do not like the dated sharp designs which we see many dentists use. We're looking for something bright and fresh while still maintaining the integrity of the profession. Elegance is not necessarily what we are going for... we need for the design to be "mature" but also up-lifting.

See our logo.
Updates

Project Deadline Extended
Reason: We have 5 designs which we like. But we'd like to see a few more before committing to a design.

Project Deadline Extended
Reason: We are awaiting revisions to this project. We are still welcoming designs while we wait to see if designers are able to provide to us the revisions we require in order to proceed with a selection.

Target Market(s)

Younger families - ages late 20's to early 40's

Industry/Entity Type

Business

Contact Information for Business Card

Marlow T. Venn DDS 2737 S. Fennimore Ave. Ste. 8 Royal Oak, MI 48059 (248)555-0174 FX (248)555-0189 info@BrightwaveDentalMi.example BrigthwaveDentalMi.example on the back of the card we need an appointment reminder (For____ Date___ Time____) with "If you are unable to keep your appointment, kindly give 48 hours notice" at the bottom. No use of teeth in the design. DOUBLE SIDED DESIGN

Requirements
Should not have
• The use of pictures of teeth

```html
<!DOCTYPE html>
<html lang="en">
<head>
<meta charset="utf-8">
<title>Brightwave Dental Care – Business Card</title>
<link rel="stylesheet" href="https://fonts.googleapis.com/css2?family=Source+Sans+3:wght@400;600&display=swap">
<style>
  :root {
    --backdrop: #7c7f84;
    --card: #e4f0c6;
    --band: #2f7a46;
    --ink: #2c6a3b;
    --accent: #5cb14b;
    --band-text: #e4f0c6;
  }
  * { margin: 0; padding: 0; box-sizing: border-box; }
  html, body { width: 1200px; height: 1200px; overflow: hidden; }
  body {
    background: var(--backdrop);
    font-family: "Source Sans 3", "Myriad Pro", Arial, sans-serif;
    position: relative;
  }
  .card {
    position: absolute;
    left: 260px;
    width: 680px;
    background: var(--card);
    box-shadow: 0 14px 24px rgba(0,0,0,0.35);
    overflow: hidden;
  }
  .card--front { top: 160px; height: 396px; }
  .card--back { top: 620px; height: 390px; }

  .band {
    position: absolute;
    left: 0; right: 0; bottom: 0;
    background: var(--band);
    color: var(--band-text);
    text-align: center;
  }
  .card--front .band { height: 52px; line-height: 52px; font-size: 25px; }
  .card--back .band { height: 76px; padding-top: 8px; font-size: 22px; line-height: 30px; }

  .brand {
    position: absolute;
    color: var(--ink);
    font-weight: 600;
    line-height: 1;
    white-space: nowrap;
  }
  .card--front .brand { left: 30px; top: 150px; font-size: 25px; }

  .divider {
    position: absolute;
    left: 298px; top: 50px;
    width: 3px; height: 250px;
    background: var(--accent);
  }
  .contact {
    position: absolute;
    left: 320px; top: 82px;
    list-style: none;
    color: var(--ink);
    font-size: 20px;
    line-height: 30px;
  }
  .contact li { display: flex; align-items: flex-start; gap: 10px; }
  .contact svg { width: 18px; height: 18px; margin-top: 6px; flex: none; fill: var(--ink); }
  .contact .address { line-height: 27px; }

  .appointment {
    position: absolute;
    top: 152px; left: 0; right: 0;
    text-align: center;
    color: var(--ink);
    font-size: 30px;
    word-spacing: 8px;
  }
  .card--back .brand { left: 0; right: 0; text-align: center; top: 244px; font-size: 19px; }
</style>
</head>
<body>

<section class="card card--front">
  <p class="brand">Brightwave Dental Care</p>
  <div class="divider"></div>
  <ul class="contact">
    <li>
      <svg viewBox="0 0 20 20" aria-hidden="true"><path d="M5 2l3 4-2 2c1 2.5 3.5 5 6 6l2-2 4 3-2 3C9 18 2 11 2 4z"/></svg>
      <span>(248)555-0174</span>
    </li>
    <li>
      <svg viewBox="0 0 20 20" aria-hidden="true"><path d="M5 2h10v5H5zM2 8h16v7h-3v3H5v-3H2zm5 5v3h6v-3z"/></svg>
      <span>(248)555-0189</span>
    </li>
    <li>
      <svg viewBox="0 0 20 20" aria-hidden="true"><path d="M10 1a9 9 0 1 0 0 18 9 9 0 0 0 0-18zM5 6h10v8H5zm1 1.2V13h8V7.2l-4 3z" fill-rule="evenodd"/></svg>
      <span>info@BrightwaveDentalMi.example</span>
    </li>
    <li>
      <svg viewBox="0 0 20 20" aria-hidden="true"><path d="M10 2l9 8h-3v8h-4v-5H8v5H4v-8H1z"/></svg>
      <span class="address">2737 S. Fennimore Ave.<br>Ste. 8 Larkmoor,<br>OR 97059.</span>
    </li>
  </ul>
  <div class="band">BrigthwaveDentalMi.example</div>
</section>

<section class="card card--back">
  <p class="appointment">( For_____ Date ____ Time____ )</p>
  <p class="brand">Brightwave Dental Care</p>
  <div class="band">“If you are unable to keep your appointment,<br>kindly give 48 hours notice”</div>
</section>

</body>
</html>
```